Something clear, simple easy to read, not to busy, gets straight to the point.

Keystone Lane Property Management specializes in single family homes. We offer property owners full Real Estate residential services. We provide the highest quality management service using state-of-the-art technology to keep them informed of how their investments are doing in real time, while providing tenants of these properties real time access to maintenance requests and billing.
Residential management includes but not limited to;
*tenant screening
*leasing
*monthly rent collection,
*property maintenance coordination
*financial reporting

Give us a call at (916) 555-0147 to see how we can work for you.

Save this card just in case.

Please add address and name on Back.
Martin Delacroix
Keystone Lane Property Management & Services
4715 Orlen Rd. C184,
Sacramento CA. 95899
Cell 916-555-0147
www.KeystoneLane.biz
BRE#04392758

Target Market(s)

Investors, property owners, Sacramento CA. USA

Industry/Entity Type

Property Management

Requirements
Must have
• Logo
Should not have
• not to busy.

```html
<!DOCTYPE html>
<html lang="en">
<head>
<meta charset="utf-8">
<title>Keystone Lane – Postcards</title>
<link href="https://fonts.googleapis.com/css2?family=Marcellus&family=Tinos&display=swap" rel="stylesheet">
<style>
  :root {
    --backdrop: #e6e6e6;
    --paper: #ffffff;
    --brand-red: #9a1c20;
    --deep-red: #5e0508;
    --darkest: #1e0203;
    --ink: #222222;
    --muted: #444444;
    --rule: #b7b7b7;
  }
  * { margin: 0; padding: 0; box-sizing: border-box; }
  html, body { width: 800px; height: 1200px; overflow: hidden; background: var(--backdrop); }
  body { position: relative; font-family: "Marcellus", serif; }

  .card {
    position: absolute; left: 208px; width: 390px; height: 302px;
    background: var(--paper); overflow: hidden;
    box-shadow: 0 0 2px rgba(0,0,0,0.12);
  }
  .card--front { top: 99px; }
  .card--info { top: 440px; }
  .card--back { top: 782px; }

  /* brand lockup */
  .brand { position: absolute; left: 0; right: 0; text-align: center; color: var(--brand-red); }
  .brand__row { display: inline-flex; align-items: center; gap: 8px; }
  .brand__square { width: 22px; height: 22px; background: var(--brand-red); display: inline-block; }
  .brand__name { font-family: "Marcellus", serif; letter-spacing: 0.5px; }
  .brand__tagline { font-family: "Marcellus", serif; color: var(--ink); letter-spacing: 0.4px; }

  .card--front .brand { top: 52px; }
  .card--front .brand__row { flex-direction: column; gap: 8px; }
  .card--front .brand__name { font-size: 18px; line-height: 1; }
  .card--front .brand__tagline { font-size: 5.6px; margin-top: 3px; }

  .card--info .brand { top: 24px; }
  .card--info .brand__square { width: 34px; height: 34px; }
  .card--info .brand__stack { text-align: left; }
  .card--info .brand__name { font-size: 27px; line-height: 1; display: block; }
  .card--info .brand__tagline { font-size: 8.6px; display: block; margin-top: 3px; }

  /* red panel */
  .panel { position: absolute; left: 0; right: 0; bottom: 0; color: #fff; }
  .card--front .panel {
    top: 149px; border-top: 2.5px solid var(--rule);
    background: linear-gradient(100deg, var(--brand-red) 0%, var(--deep-red) 45%, var(--darkest) 100%);
  }
  .card--info .panel { top: 90px; background: var(--brand-red); }

  .services {
    position: absolute; left: 0; right: 0; height: 74px; text-align: center;
  }
  .card--front .services {
    top: 29px;
    background: linear-gradient(90deg, rgba(30,2,3,0.85), rgba(30,2,3,0.55) 60%, rgba(30,2,3,0.85));
  }
  .card--info .services {
    top: 100px;
    background: linear-gradient(90deg, var(--darkest) 0%, rgba(40,3,4,0.9) 55%, var(--brand-red) 100%);
  }
  .services__list { font-size: 13.6px; line-height: 17px; padding-top: 9px; }
  .services__call { font-size: 10.4px; margin-top: 5px; }

  .keep-note {
    position: absolute; left: 0; right: 0; text-align: center;
    font-size: 7.4px; font-variant: small-caps; letter-spacing: 0.4px;
  }
  .card--front .keep-note { top: 123px; }
  .card--info .keep-note { top: 186px; }

  .about { position: absolute; left: 35px; right: 40px; top: 12px; font-size: 9.1px; line-height: 10.8px; }
  .about p { margin-bottom: 7px; }

  /* back */
  .contact { position: absolute; left: 20px; top: 16px; font-family: "Tinos", serif; color: var(--muted); font-size: 8.6px; line-height: 10.6px; }
  .contact__name { font-size: 11.2px; color: var(--ink); margin-bottom: 3px; }
  .contact__gap { margin-top: 3px; }
  .back-mark {
    position: absolute; left: 10px; top: 150px;
    display: flex; align-items: center; gap: 10px;
    color: rgba(154,28,32,0.09); font-size: 34px; font-family: "Marcellus", serif;
  }
  .back-mark__square { width: 60px; height: 60px; background: rgba(154,28,32,0.07); }
</style>
</head>
<body>

<section class="card card--front">
  <div class="brand">
    <div class="brand__row">
      <span class="brand__square"></span>
      <div>
        <div class="brand__name">KEYSTONE LANE</div>
        <div class="brand__tagline">PROPERTY MANAGEMENT &amp; SERVICES</div>
      </div>
    </div>
  </div>
  <div class="panel">
    <div class="services">
      <div class="services__list">Tenant Screening, Leasing, Monthly Rent Collection,<br>Property Maintenance Coordination, Financial Reporting</div>
      <div class="services__call">Give us a call at (916) 555-0147 to see how we can work for you.</div>
    </div>
    <div class="keep-note">Save this card just in case.</div>
  </div>
</section>

<section class="card card--info">
  <div class="brand">
    <div class="brand__row">
      <span class="brand__square"></span>
      <div class="brand__stack">
        <span class="brand__name">KEYSTONE LANE</span>
        <span class="brand__tagline">PROPERTY MANAGEMENT &amp; SERVICES</span>
      </div>
    </div>
  </div>
  <div class="panel">
    <div class="about">
      <p>Keystone Lane Property Management specializes in single family homes.</p>
      <p>We offer property owners full Real Estate residential services.</p>
      <p>We provide the highest quality management service using state-of-the-art technology to keep them informed of how their investments are doing in real time, while providing tenants of these properties real time access to maintenance requests and billing.</p>
    </div>
    <div class="services">
      <div class="services__list">Tenant Screening, Leasing, Monthly Rent Collection,<br>Property Maintenance Coordination, Financial Reporting</div>
      <div class="services__call">Give us a call at (916) 555-0147 to see how we can work for you.</div>
    </div>
    <div class="keep-note">Save this card just in case.</div>
  </div>
</section>

<section class="card card--back">
  <div class="contact">
    <div class="contact__name">Martin Delacroix</div>
    <div>Keystone Lane Property Management &amp; Services</div>
    <div>4715 Orlen Rd. C184, Sacramento CA. 95899</div>
    <div>Cell 916-555-0147</div>
    <div class="contact__gap">www.KeystoneLane.biz</div>
    <div class="contact__gap">BRE#04392758</div>
  </div>
  <div class="back-mark">
    <span class="back-mark__square"></span>
    <span>KEYSTONE LANE</span>
  </div>
</section>

</body>
</html>
```